Enhance the web site presence of Kolrith Global Limited

Upgrade the current web site www.kolrithpanel.com to share with the audience our current plan and future developments of our company. I have created a worksheet which shows all the pages that I like to have. The home page in English, Japanese and Chinese is hyperlinked to the various pages. Under the product, we should allow the user to select "single sided PCB or double sided PCB". The translation of the contents of the pages with Japanese is not complete but the English and Chinese are complete. You can download the briefing and photos in the dropbox files below;

https://www.sharelocker.net/sh/xk4trw92mpd3ab1/BBQm_Lp841zzPq2Rw7KtYnHjEa?dl=0

Target Market(s)

Electronic companies

Industry/Entity Type

Electronic

Coding

Coded - Design and coding required

Number of Pages Required

5+ page

Font styles to use
Sans Serif

Colors
00a990
0353a1
33b8a4

Requirements
Must have
• Get a sense of confidence on our company's integrity and capability to deliver the highest quality PCBs with the most competitive prices and best services. A sense of elegance is essential as we DON'T treat profits as the number one goal. Our number goal is to do the RIGHT things right. Having a mixture of our company photos will be appropriate.

```html
<!DOCTYPE html>
<html lang="en">
<head>
<meta charset="utf-8">
<title>Kolrith Global Limited</title>
<link href="https://fonts.googleapis.com/css2?family=Oswald:wght@300;500;600&family=Poppins:ital,wght@0,300;0,400;0,500;1,400&display=swap" rel="stylesheet">
<style>
:root{
  --green:#1e7a4c;
  --green-dark:#17603b;
  --ink:#1c1c1c;
  --text:#555;
  --grey-panel:#e6e5e5;
  --footer:#252525;
  --footer-text:#d0d0d0;
  --white:#fff;
}
*{box-sizing:border-box;margin:0;padding:0}
html,body{width:1200px;height:3327px;overflow:hidden}
body{position:relative;background:var(--white);font-family:'Poppins',sans-serif;color:var(--ink)}
.abs{position:absolute}
.topline{left:0;top:0;width:1200px;height:5px;background:var(--green-dark)}
.brand{left:85px;top:26px}
.brand-name{display:flex;align-items:center;gap:10px;font-size:30px;font-weight:500;color:var(--ink);letter-spacing:1px;line-height:1}
.brand-name span.sq{width:16px;height:16px;background:var(--green)}
.brand-tag{font-size:9px;color:var(--ink);margin-top:8px;letter-spacing:.4px}
.account{left:775px;top:24px;font-size:12px;display:flex;align-items:center;gap:8px;color:var(--ink)}
.lang{left:990px;top:22px;font-size:11px;display:flex;align-items:center;gap:8px}
.head-rule{left:740px;top:60px;width:375px;height:1px;background:#ddd}
.head-vr{left:958px;top:12px;width:1px;height:44px;background:#ddd}
.nav{top:78px;right:86px;display:flex;gap:48px;font-size:12.5px;font-weight:500;letter-spacing:.3px}
.hero{left:0;top:108px;width:1200px;height:654px;background:radial-gradient(ellipse at 82% 40%,#2a6d92 0%,#0f2a44 35%,#060d18 70%,#03060c 100%)}
.hero-title{left:85px;top:300px;font-family:'Oswald',sans-serif;font-weight:500;font-size:46px;line-height:72px;color:var(--white);letter-spacing:1.5px}
.hero-sub{left:85px;top:448px;font-family:'Oswald',sans-serif;font-weight:300;font-size:30px;color:var(--white);letter-spacing:1px;display:flex;align-items:center;gap:22px}
.hero-sub i{display:block;width:108px;height:2px;background:#ccc}
.btn{display:flex;align-items:center;justify-content:center;background:var(--green);color:var(--white);font-weight:500}
.hero-btn{top:531px;width:190px;height:59px;font-size:19px}
.photo{display:block}
.bg-photo{left:0;top:783px;width:585px;height:331px;background:linear-gradient(135deg,#dcdfe2,#9fa8b0 55%,#5d6e86)}
.bg-panel{left:608px;top:783px;width:592px;height:331px;background:var(--grey-panel)}
.h2{font-size:31px;font-weight:500;color:var(--ink)}
.accent{height:3px;width:32px;background:var(--green)}
.bg-text{font-size:12.5px;line-height:23px;color:var(--text);width:455px}
.small-btn{height:43px;width:127px;font-size:12px}
.center-title{width:1200px;text-align:center;left:0}
.center-rule{left:536px;width:128px;height:2px;background:#bbb}
.center-rule::after{content:"";position:absolute;left:48px;top:-1px;width:32px;height:4px;background:var(--green)}
.prod-img{top:1306px;width:502px;height:264px}
.prod-title{top:1590px;width:480px;font-size:19.5px;font-weight:500;line-height:36px;letter-spacing:.3px}
.prod-rule{top:1683px;width:32px;height:3px;background:var(--green)}
.prod-text{top:1705px;width:500px;font-size:13px;line-height:27px;color:var(--text)}
.quote-panel{left:0;top:1925px;width:585px;height:332px;background:var(--grey-panel)}
.quote-text{left:82px;top:2003px;width:300px;font-size:16.5px;line-height:32px;color:#333}
.quote-name{left:82px;top:2155px;font-size:20px;font-weight:500}
.quote-role{left:85px;top:2190px;font-size:19px;font-style:italic;color:var(--green)}
.people{left:395px;top:2010px;width:190px;height:247px;background:linear-gradient(160deg,#f1d46b,#c7b08a 45%,#5d6a85)}
.form-panel{left:610px;top:1925px;width:590px;height:332px;background:var(--green)}
.form-title{left:668px;top:1958px;font-size:30px;color:var(--white);display:flex;align-items:center;gap:20px}
.form-title i{display:block;width:125px;height:1px;background:#bfe0cf}
.field{width:208px;height:49px;border:1px solid #cfe6da;color:var(--white);font-size:12.5px;padding-left:18px;display:flex;align-items:center}
.submit{left:670px;top:2163px;width:438px;height:50px;background:var(--green-dark);color:var(--white);font-size:19px;display:flex;align-items:center;justify-content:center}
.news-img{top:2468px;width:323px;height:204px}
.news-date{top:2638px;width:115px;height:34px;font-size:15px;font-weight:500}
.news-meta{top:2698px;width:323px;text-align:center;font-size:13.5px;color:#444}
.news-meta b{font-weight:400;color:#bbb;margin:0 16px}
.news-title{top:2743px;width:323px;text-align:center;font-size:18.5px;line-height:32px;color:#222}
.footer{left:0;top:2915px;width:1200px;height:360px;background:var(--footer)}
.foot-head{top:2984px;font-size:15.5px;color:var(--footer-text)}
.foot-rule{top:3013px;width:58px;height:2px;background:var(--green)}
.foot-row{display:flex;gap:18px;align-items:flex-start;font-size:12.5px;line-height:22px;color:var(--footer-text)}
.ico{flex:none;width:26px;height:26px;border-radius:50%;background:#3a3a3a;display:flex;align-items:center;justify-content:center}
.news-input{left:902px;top:3035px;width:161px;height:34px;border:1px solid #555;font-size:12px;color:#aaa;display:flex;align-items:center;padding-left:14px}
.go{left:1068px;top:3035px;width:45px;height:34px;font-size:12px}
.socials{left:902px;top:3097px;display:flex;gap:12px}
.socials span{width:22px;height:22px;border-radius:50%;background:#f2f2f2}
.copy{left:0;top:3275px;width:1200px;height:52px;background:var(--green);color:#cfe7da;font-size:11px;display:flex;align-items:center;justify-content:center}
</style>
</head>
<body>
<header>
  <div class="abs topline"></div>
  <div class="abs brand">
    <div class="brand-name"><span class="sq"></span>Kolrith Global</div>
    <div class="brand-tag">Printed Circuit Boards is Our Business</div>
  </div>
  <div class="abs account">
    <svg width="16" height="16" viewBox="0 0 16 16" fill="none" stroke="#1e7a4c" stroke-width="1.6"><path d="M2 8h8M7 5l3 3-3 3M10 2h4v12h-4"/></svg>
    <span style="margin-left:8px">LOGIN</span><span>/</span><span>REGISTER</span>
  </div>
  <div class="abs head-vr"></div>
  <div class="abs lang">ENGLISH
    <svg width="34" height="22" viewBox="0 0 34 22"><rect width="34" height="22" fill="#1f3b8c"/><path d="M0 0L34 22M34 0L0 22" stroke="#fff" stroke-width="4"/><path d="M0 0L34 22M34 0L0 22" stroke="#c8102e" stroke-width="1.5"/><path d="M17 0v22M0 11h34" stroke="#fff" stroke-width="6"/><path d="M17 0v22M0 11h34" stroke="#c8102e" stroke-width="3"/></svg>
    <svg width="9" height="6" viewBox="0 0 9 6"><path d="M0 0h9L4.5 6z" fill="#999"/></svg>
  </div>
  <div class="abs head-rule"></div>
  <nav class="abs nav"><span>HOME</span><span>PRODUCTS</span><span>OUR FACILITIES</span><span>NEWS</span><span>CUSTOMERS</span><span>CONTACT US</span></nav>
</header>

<section class="abs hero" role="img" aria-label="Glowing blue network of connected nodes on a dark background"></section>
<h1 class="abs hero-title">WE'RE THE<br>CURRENT SPECIALIST!</h1>
<div class="abs hero-sub">KEEPING YOU WIRED <i></i></div>
<a class="abs btn hero-btn" style="left:85px">KNOW MORE</a>
<a class="abs btn hero-btn" style="left:307px">CONTACT US</a>

<div class="abs bg-photo photo" role="img" aria-label="Technician in blue uniform operating a circuit board production machine"></div>
<section class="abs bg-panel"></section>
<h2 class="abs h2" style="left:656px;top:820px">COMPANY BACKGROUND</h2>
<div class="abs accent" style="left:658px;top:880px"></div>
<p class="abs bg-text" style="left:658px;top:903px">Established in 2007, Kolrith Global Limited (KGL) is a Hong Kong company specializing in single and double sized printed circuit boards. Its manufacturing facility is located in a self-owned facility in Tangxia, Dongguan of China which is 50 minutes from Hong Kong.</p>
<a class="abs btn small-btn" style="left:658px;top:1036px">LEARN MORE</a>

<h2 class="abs h2 center-title" style="top:1192px">OUR PRODUCTS</h2>
<div class="abs center-rule" style="top:1254px"></div>
<div class="abs prod-img photo" style="left:85px;background:linear-gradient(180deg,#dfe2dc,#a9b0a4 60%,#7d8275)" role="img" aria-label="Single layer circuit boards on a production conveyor"></div>
<div class="abs prod-img photo" style="left:610px;background:linear-gradient(180deg,#cfcac2,#c4a58a 55%,#e27a4c)" role="img" aria-label="Stacks of boards in front of an industrial press line"></div>
<h3 class="abs prod-title" style="left:85px;width:360px">SINGLE LAYERED PRINTED CIRCUIT BOARDS</h3>
<h3 class="abs prod-title" style="left:610px">DOUBLE LAYERED AND MULTI-LAYERED PRINTED CIRCUIT BOARDS</h3>
<div class="abs prod-rule" style="left:85px"></div>
<div class="abs prod-rule" style="left:610px"></div>
<p class="abs prod-text" style="left:85px">We are offering single layered circuit boards through our own production facility in China for customers in the following industries</p>
<p class="abs prod-text" style="left:610px">We are offering single layered circuit boards through our own production facility in China for customers in the following industries</p>
<a class="abs btn small-btn" style="left:85px;top:1793px">LEARN MORE</a>
<a class="abs btn small-btn" style="left:610px;top:1793px">LEARN MORE</a>

<section class="abs quote-panel"></section>
<svg class="abs" style="left:82px;top:1952px" width="56" height="40" viewBox="0 0 56 40" fill="#cfcfcf"><path d="M0 40V20L12 0h9L14 18h10v22zM30 40V20L42 0h9L44 18h10v22z"/></svg>
<svg class="abs" style="left:300px;top:2118px" width="56" height="40" viewBox="0 0 56 40" fill="#cfcfcf"><path d="M56 0v20L44 40h-9l7-18H32V0zM26 0v20L14 40H5l7-18H2V0z"/></svg>
<p class="abs quote-text">It is a long established fact that a reader will be distracted by the readable content of a page when looking at its layout.</p>
<div class="abs quote-name">Aren Holt,</div>
<div class="abs quote-role">Businessman</div>
<div class="abs people photo" role="img" aria-label="Two engineers in yellow hard hats holding a clipboard"></div>

<section class="abs form-panel"></section>
<div class="abs form-title">Schedule Services <i></i></div>
<div class="abs field" style="left:670px;top:2030px">Name...</div>
<div class="abs field" style="left:900px;top:2030px">Email Id...</div>
<div class="abs field" style="left:670px;top:2098px">Phone No...</div>
<div class="abs field" style="left:900px;top:2098px">Company &nbsp;Name</div>
<div class="abs submit">Submit</div>

<h2 class="abs h2 center-title" style="top:2352px">OUR RECENT NEWS</h2>
<div class="abs center-rule" style="top:2413px"></div>
<div class="abs news-img photo" style="left:85px;background:linear-gradient(135deg,#eef0ee,#b9c0bc 55%,#52667a)" role="img" aria-label="Worker beside a white reflow oven on the factory floor"></div>
<div class="abs news-img photo" style="left:437px;background:linear-gradient(135deg,#e4e8e5,#aab3ad 55%,#6b7a70)" role="img" aria-label="Screen printing machine inside the plant"></div>
<div class="abs news-img photo" style="left:790px;background:linear-gradient(180deg,#4aa6e0,#bfe1f2 45%,#8dc86c 70%,#eeeeee)" role="img" aria-label="Factory building under a blue sky"></div>
<div class="abs btn news-date" style="left:190px">Jul 27, 2016</div>
<div class="abs btn news-date" style="left:543px">Jul 27, 2016</div>
<div class="abs btn news-date" style="left:896px">Jul 27, 2016</div>
<div class="abs news-meta" style="left:85px">By Mira Calloway<b>|</b>3 comments</div>
<div class="abs news-meta" style="left:437px">By Mira Calloway<b>|</b>3 comments</div>
<div class="abs news-meta" style="left:790px">By Mira Calloway<b>|</b>3 comments</div>
<h4 class="abs news-title" style="left:85px;font-weight:400">An occasion that joins two hearts in a symphony</h4>
<h4 class="abs news-title" style="left:437px;font-weight:400">An occasion that joins two hearts in a symphony</h4>
<h4 class="abs news-title" style="left:790px;font-weight:400">An occasion that joins two hearts in a symphony</h4>

<footer>
  <div class="abs footer"></div>
  <div class="abs foot-head" style="left:85px">Contact information</div>
  <div class="abs foot-head" style="left:483px">Contact information</div>
  <div class="abs foot-head" style="left:902px">Newsletter</div>
  <div class="abs foot-rule" style="left:85px"></div>
  <div class="abs foot-rule" style="left:483px"></div>
  <div class="abs foot-rule" style="left:902px"></div>

  <div class="abs foot-row" style="left:85px;top:3035px;width:330px">
    <span class="ico"><svg width="10" height="14" viewBox="0 0 10 14"><path d="M5 0a5 5 0 0 1 5 5c0 4-5 9-5 9S0 9 0 5a5 5 0 0 1 5-5z" fill="#fff"/><circle cx="5" cy="5" r="2" fill="#3a3a3a"/></svg></span>
    <span>Kolrith Global Limited 28/F Marlow Tower 17 Kestrel Road Causeway Bay,<br>HONG KONG</span>
  </div>
  <div class="abs foot-row" style="left:85px;top:3128px">
    <span class="ico"><svg width="12" height="12" viewBox="0 0 12 12"><path d="M2 0l3 3-1.5 2A7 7 0 0 0 7 8.5L9 7l3 3-2 2C5 12 0 7 0 2z" fill="#fff"/></svg></span>
    <span style="padding-top:2px">+852-30004512</span>
  </div>
  <div class="abs foot-row" style="left:85px;top:3173px">
    <span class="ico"><svg width="12" height="9" viewBox="0 0 12 9"><rect width="12" height="9" fill="#fff"/><path d="M0 0l6 5 6-5" stroke="#3a3a3a" fill="none"/></svg></span>
    <span style="padding-top:2px">sales@kolrithpanel.com</span>
  </div>

  <div class="abs foot-row" style="left:483px;top:3035px;width:360px">
    <span class="ico"><svg width="10" height="14" viewBox="0 0 10 14"><path d="M5 0a5 5 0 0 1 5 5c0 4-5 9-5 9S0 9 0 5a5 5 0 0 1 5-5z" fill="#fff"/><circle cx="5" cy="5" r="2" fill="#3a3a3a"/></svg></span>
    <span>Kolrith Global (Dongguan) Limited 9 Lanfeng East 4 Road Qiaoxi Township, Dongguan Guangdong Province, China 523990</span>
  </div>
  <div class="abs foot-row" style="left:483px;top:3128px">
    <span class="ico"><svg width="12" height="12" viewBox="0 0 12 12"><path d="M2 0l3 3-1.5 2A7 7 0 0 0 7 8.5L9 7l3 3-2 2C5 12 0 7 0 2z" fill="#fff"/></svg></span>
    <span style="padding-top:2px">+86-760</span>
  </div>
  <div class="abs foot-row" style="left:483px;top:3173px">
    <span class="ico"><svg width="12" height="9" viewBox="0 0 12 9"><rect width="12" height="9" fill="#fff"/><path d="M0 0l6 5 6-5" stroke="#3a3a3a" fill="none"/></svg></span>
    <span style="padding-top:2px">sales@kolrithpanel.com</span>
  </div>

  <div class="abs news-input">Your Email Id...</div>
  <div class="abs btn go">GO</div>
  <div class="abs socials"><span></span><span></span><span></span><span></span></div>
  <div class="abs copy">Copyright © 2017, Kolrith Global Limited. All Rights Reserved</div>
</footer>
</body>
</html>
```